Important infographic for my new website

I am making a new website for my company: Brovo Tutoring Systems. Brovo Tutoring Systems is a platform where we allow our customers (Language schools, etc.) to connect with their students through already installed IM (instant messaging apps) like Chatterly, TalkNest, Pindo, etc.

This is a very important page, since this is the first thing people will see.
1) Please look at attached powerpoint file. Go to slide 1.

2) This is an important infographic that will go after the main cover page of the website

3) The logo will go in the middle

4) This is a general idea... I made this to give you a general idea. Please show me some options

Target Market(s)

Language schools and language related businesses - schools teaching English, training people to speak english

Industry/Entity Type

Education

Requirements
Must have
• I need all the files that will allow this to look good on a website... it has to fit nicely and clearly the whole screen...
Nice to have
• Please review my attached files... i would like the elements shown in my file, but please be creative... this is a very important page.
• I'm not sure about the background color... it could be white... especially if all the other elements are going to have color....

```html
<!DOCTYPE html>
<html lang="en">
<head>
<meta charset="utf-8">
<title>What We Do – Brovo Tutoring Systems</title>
<link rel="stylesheet" href="https://fonts.googleapis.com/css2?family=Oswald:wght@500;600&display=swap">
<style>
  :root {
    --bg-centre: #f7f7f8;
    --bg-edge: #d6d7da;
    --brand-blue: #3b5fae;
    --hub-blue: #2a82c6;
    --learner-green: #7cbf3d;
    --learner-green-dark: #5aa532;
    --apps-cyan: #1ba6cc;
    --apps-cyan-dark: #1790b8;
    --business-orange: #f26522;
    --business-orange-dark: #e2501a;
    --white: #ffffff;
    --ink-muted: #4a4f5a;
  }
  * { box-sizing: border-box; margin: 0; padding: 0; }
  html, body { width: 1200px; height: 614px; overflow: hidden; }
  body {
    font-family: "Oswald", "Arial Narrow", sans-serif;
    background: var(--bg-edge);
  }
  .canvas {
    position: relative;
    width: 1200px;
    height: 614px;
    overflow: hidden;
    background: radial-gradient(ellipse at 52% 55%, var(--bg-centre) 0%, #eeeef0 45%, var(--bg-edge) 100%);
  }
  .title-tab {
    position: absolute;
    left: 475px; top: 0;
    width: 296px; height: 78px;
    background: var(--brand-blue);
    border-radius: 0 0 12px 12px;
    color: var(--white);
    font-weight: 600;
    font-size: 46px;
    line-height: 78px;
    text-align: center;
    letter-spacing: 0.5px;
  }
  .hub-diagram { position: absolute; inset: 0; }
  .band {
    position: absolute;
    height: 46px;
    color: var(--white);
    font-weight: 600;
    font-size: 32px;
    line-height: 46px;
    white-space: nowrap;
  }
  .band--learner {
    left: 0; top: 205px; width: 309px;
    padding-left: 32px;
    background: linear-gradient(90deg, var(--learner-green-dark), var(--learner-green));
    clip-path: polygon(0 0, 96% 0, 100% 100%, 0 100%);
  }
  .band--apps {
    left: 0; top: 390px; width: 309px;
    padding-left: 32px;
    background: linear-gradient(90deg, var(--apps-cyan-dark), var(--apps-cyan));
    clip-path: polygon(0 0, 96% 0, 100% 100%, 0 100%);
  }
  .band--business {
    left: 909px; top: 305px; width: 291px;
    padding-left: 18px;
    background: linear-gradient(90deg, var(--business-orange), var(--business-orange-dark));
    clip-path: polygon(4% 0, 100% 0, 100% 100%, 0 100%);
  }
  .apps-frame {
    position: absolute;
    left: 20px; top: 436px;
    width: 259px; height: 109px;
    border: 3px solid var(--hub-blue);
    border-top: none;
    border-radius: 0 0 14px 14px;
    display: grid;
    grid-template-columns: repeat(3, 1fr);
    align-content: center;
    row-gap: 16px;
    padding: 6px 10px;
  }
  .app-name {
    display: flex;
    align-items: center;
    gap: 5px;
    font-weight: 500;
    font-size: 14px;
    color: var(--ink-muted);
  }
  .app-name::before {
    content: "";
    width: 22px; height: 22px;
    border-radius: 50%;
    background: var(--apps-cyan);
    flex: none;
  }
  .hub-logo {
    position: absolute;
    left: 537px; top: 300px;
    width: 200px;
    text-align: center;
    color: var(--brand-blue);
    font-weight: 600;
    line-height: 1.05;
  }
  .hub-logo__lead { font-size: 44px; display: block; }
  .hub-logo__rest { font-size: 21px; display: block; letter-spacing: 1px; }
  .illustration { position: absolute; }
  .illustration--learners {
    left: 42px; top: 97px; width: 226px; height: 106px;
    background: linear-gradient(90deg, #c9a88a, #8a9bb0, #e1a07a);
    border-radius: 10px;
    opacity: 0.75;
  }
  .illustration--school {
    left: 951px; top: 97px; width: 189px; height: 180px;
    background: linear-gradient(180deg, #c0392b 0%, #c0392b 22%, #e9c98e 22%, #d9b272 85%, #6fb33f 85%);
    border-radius: 8px;
    opacity: 0.85;
  }
  .illustration--teacher {
    left: 951px; top: 369px; width: 194px; height: 222px;
    background: linear-gradient(90deg, #2c5a3a 0%, #2c5a3a 62%, #c9a2d6 62%, #5a4f8a 100%);
    border-radius: 8px;
    opacity: 0.85;
  }
</style>
</head>
<body>
<main class="canvas">

  <div class="illustration illustration--learners" role="img" aria-label="Illustration of a group of six language learners standing side by side"></div>
  <div class="illustration illustration--school" role="img" aria-label="Illustration of a language school building"></div>
  <div class="illustration illustration--teacher" role="img" aria-label="Illustration of a teacher holding a book beside a chalkboard"></div>

  <svg class="hub-diagram" width="1200" height="614" viewBox="0 0 1200 614" aria-hidden="true">
    <g stroke="var(--hub-blue)" stroke-width="3" fill="none">
      <line x1="309" y1="231" x2="422" y2="314"/>
      <line x1="309" y1="411" x2="422" y2="338"/>
      <line x1="826" y1="325" x2="912" y2="325"/>
      <line x1="152" y1="268" x2="152" y2="374"/>
    </g>
    <g fill="var(--hub-blue)">
      <polygon points="146,272 152,262 158,272"/>
      <polygon points="146,370 152,380 158,370"/>
    </g>

    <g stroke="var(--hub-blue)" stroke-width="4">
      <line x1="637" y1="355" x2="471" y2="242"/>
      <line x1="637" y1="355" x2="510" y2="196"/>
      <line x1="637" y1="355" x2="554" y2="175"/>
      <line x1="637" y1="355" x2="620" y2="171"/>
      <line x1="637" y1="355" x2="701" y2="185"/>
      <line x1="637" y1="355" x2="752" y2="210"/>
      <line x1="637" y1="355" x2="780" y2="260"/>
      <line x1="637" y1="355" x2="798" y2="325"/>
      <line x1="637" y1="355" x2="785" y2="425"/>
      <line x1="637" y1="355" x2="734" y2="480"/>
      <line x1="637" y1="355" x2="632" y2="524"/>
      <line x1="637" y1="355" x2="545" y2="506"/>
      <line x1="637" y1="355" x2="471" y2="459"/>
      <line x1="637" y1="355" x2="448" y2="388"/>
      <line x1="637" y1="355" x2="448" y2="323"/>
    </g>

    <circle cx="637" cy="355" r="138" fill="var(--white)" stroke="var(--hub-blue)" stroke-width="8"/>

    <g class="hub-icons" fill="var(--hub-blue)">
      <!-- video -->
      <g transform="translate(471 242)">
        <circle r="28"/>
        <rect x="-12" y="-10" width="24" height="20" rx="2" fill="var(--white)"/>
        <polygon points="-4,-5 6,0 -4,5"/>
      </g>
      <!-- music -->
      <g transform="translate(510 196)">
        <circle r="28"/>
        <path d="M-2 -12 L8 -14 L8 5" stroke="var(--white)" stroke-width="3" fill="none"/>
        <line x1="-2" y1="-12" x2="-2" y2="8" stroke="var(--white)" stroke-width="3"/>
        <circle cx="-6" cy="8" r="5" fill="var(--white)"/>
        <circle cx="4" cy="6" r="5" fill="var(--white)"/>
      </g>
      <!-- speaking waves -->
      <g transform="translate(554 175)">
        <circle r="28"/>
        <circle cx="-6" cy="0" r="8" fill="var(--white)"/>
        <path d="M6 -7 A9 9 0 0 1 6 7 M10 -11 A14 14 0 0 1 10 11" stroke="var(--white)" stroke-width="2.5" fill="none"/>
      </g>
      <!-- message -->
      <g transform="translate(620 171)">
        <circle r="30"/>
        <rect x="-15" y="-12" width="24" height="16" rx="2" fill="var(--white)"/>
        <rect x="-6" y="-2" width="22" height="15" rx="2" fill="var(--white)" stroke="var(--hub-blue)" stroke-width="2"/>
        <line x1="-2" y1="4" x2="12" y2="4" stroke="var(--hub-blue)" stroke-width="2"/>
      </g>
      <!-- speaker -->
      <g transform="translate(701 185)">
        <circle r="28"/>
        <polygon points="-12,-5 -6,-5 2,-12 2,12 -6,5 -12,5" fill="var(--white)"/>
        <path d="M6 -6 A8 8 0 0 1 6 6 M10 -10 A13 13 0 0 1 10 10" stroke="var(--white)" stroke-width="2.5" fill="none"/>
      </g>
      <!-- conversation -->
      <g transform="translate(752 210)">
        <circle r="24"/>
        <ellipse cx="-3" cy="-3" rx="10" ry="7" fill="none" stroke="var(--white)" stroke-width="2.5"/>
        <ellipse cx="5" cy="5" rx="10" ry="7" fill="var(--hub-blue)" stroke="var(--white)" stroke-width="2.5"/>
      </g>
      <!-- alphabet board -->
      <g transform="translate(780 260)">
        <circle r="26"/>
        <rect x="-15" y="-10" width="30" height="20" rx="2" fill="var(--white)"/>
        <text x="0" y="5" text-anchor="middle" font-family="Oswald, sans-serif" font-size="12" font-weight="600" fill="var(--hub-blue)">ABC</text>
      </g>
      <!-- microphone -->
      <g transform="translate(798 325)">
        <circle r="28"/>
        <rect x="-5" y="-14" width="10" height="17" rx="5" fill="var(--white)"/>
        <path d="M-9 -2 A9 9 0 0 0 9 -2" stroke="var(--white)" stroke-width="2.5" fill="none"/>
        <line x1="0" y1="7" x2="0" y2="13" stroke="var(--white)" stroke-width="2.5"/>
        <line x1="-6" y1="13" x2="6" y2="13" stroke="var(--white)" stroke-width="2.5"/>
      </g>
      <!-- image -->
      <g transform="translate(785 425)">
        <circle r="28"/>
        <rect x="-14" y="-11" width="28" height="22" fill="none" stroke="var(--white)" stroke-width="2.5"/>
        <polygon points="-11,8 -3,-2 3,4 7,0 11,8" fill="var(--white)"/>
        <circle cx="6" cy="-5" r="2.5" fill="var(--white)"/>
      </g>
      <!-- approval -->
      <g transform="translate(734 480)">
        <circle r="26"/>
        <path d="M-10 0 L-3 8 L11 -8" stroke="var(--white)" stroke-width="4" fill="none"/>
      </g>
      <!-- favourite -->
      <g transform="translate(632 524)">
        <circle r="30"/>
        <path d="M0 12 L-12 0 A6.5 6.5 0 0 1 0 -8 A6.5 6.5 0 0 1 12 0 Z" fill="var(--white)"/>
      </g>
      <!-- text chat -->
      <g transform="translate(545 506)">
        <circle r="28"/>
        <circle r="13" fill="var(--white)"/>
        <g stroke="var(--hub-blue)" stroke-width="2">
          <line x1="-6" y1="-4" x2="6" y2="-4"/>
          <line x1="-6" y1="0" x2="6" y2="0"/>
          <line x1="-6" y1="4" x2="6" y2="4"/>
        </g>
      </g>
      <!-- group -->
      <g transform="translate(471 459)">
        <circle r="26"/>
        <circle cx="-5" cy="-5" r="5" fill="var(--white)"/>
        <circle cx="6" cy="-4" r="4" fill="var(--white)"/>
        <path d="M-14 10 A9 8 0 0 1 4 10 Z" fill="var(--white)"/>
        <path d="M1 9 A7 7 0 0 1 14 9 Z" fill="var(--white)"/>
      </g>
      <!-- listening -->
      <g transform="translate(448 388)">
        <circle r="28"/>
        <path d="M-4 12 C-4 4 -9 2 -9 -4 A8 8 0 0 1 7 -4" stroke="var(--white)" stroke-width="3" fill="none"/>
        <path d="M10 -10 A14 14 0 0 1 10 10" stroke="var(--white)" stroke-width="2.5" fill="none"/>
      </g>
      <!-- notes -->
      <g transform="translate(448 323)">
        <circle r="28"/>
        <rect x="-11" y="-12" width="18" height="24" rx="2" fill="none" stroke="var(--white)" stroke-width="2.5"/>
        <g stroke="var(--white)" stroke-width="2">
          <line x1="-7" y1="-5" x2="3" y2="-5"/>
          <line x1="-7" y1="0" x2="3" y2="0"/>
          <line x1="-7" y1="5" x2="0" y2="5"/>
          <line x1="12" y1="-12" x2="3" y2="6" stroke-width="3"/>
        </g>
      </g>
    </g>
  </svg>

  <h1 class="title-tab">WHAT WE DO?</h1>

  <div class="band band--learner">LANGUAGE LEARNER</div>
  <div class="band band--apps">IM MESSAGING APPS</div>
  <div class="band band--business">LANGUAGE BUSINESS</div>

  <ul class="apps-frame" aria-label="Supported messaging apps">
    <li class="app-name">TalkNest</li>
    <li class="app-name">Chatterly</li>
    <li class="app-name">Pindo</li>
    <li class="app-name">Flitmail</li>
    <li class="app-name">Yappa</li>
    <li class="app-name">Murmur</li>
  </ul>

  <div class="hub-logo">
    <span class="hub-logo__lead">BROVO</span>
    <span class="hub-logo__rest">TUTORING SYSTEMS</span>
  </div>

</main>
</body>
</html>
```